Castlereagh Yard Works L.L.C.
Repair Maintenance Improvement
Professional
Patrick Dunleavy
do not want address
pat@castlereaghyardworks.example
Thank You!
The finest compliment I could ever receive is a referral from my friends and customers.

```html
<!DOCTYPE html>
<html lang="en">
<head>
<meta charset="utf-8">
<title>Castlereagh Yard Works L.L.C. — Business Card</title>
<link rel="stylesheet" href="https://fonts.googleapis.com/css2?family=Roboto:wght@400&display=swap">
<style>
  :root {
    --page-bg: #3b3b3b;
    --card-light: #f6f6f6;
    --card-mid: #e4e4e4;
    --card-edge: #d2d2d2;
    --brand-green: #587566;
    --ink: #1f1f1f;
    --white: #ffffff;
  }
  * { margin: 0; padding: 0; box-sizing: border-box; }
  html, body {
    width: 1200px;
    height: 826px;
    overflow: hidden;
    background: var(--page-bg);
  }
  .canvas {
    position: relative;
    width: 1200px;
    height: 826px;
  }
  .business-card {
    position: absolute;
    left: 173px;
    top: 240px;
    width: 864px;
    height: 422px;
    border-radius: 28px;
    overflow: hidden;
    background: linear-gradient(160deg, var(--card-light) 0%, var(--card-mid) 60%, var(--card-edge) 100%);
  }
  .brand-block {
    position: absolute;
    left: 340px;
    top: 92px;
    width: 490px;
    text-align: center;
    font-family: "Roboto", sans-serif;
    font-weight: 400;
  }
  .brand-name {
    font-size: 33px;
    line-height: 1.2;
    color: var(--brand-green);
  }
  .brand-tagline {
    margin-top: 18px;
    font-size: 17px;
    letter-spacing: 1px;
    color: var(--ink);
  }
  .name-band {
    position: absolute;
    left: 0;
    top: 264px;
    width: 100%;
    height: 43px;
    background: var(--brand-green);
  }
  .holder-name {
    position: absolute;
    left: 55px;
    top: 0;
    line-height: 43px;
    font-family: "Roboto", sans-serif;
    font-size: 29px;
    letter-spacing: 1px;
    color: var(--white);
  }
  .contact-list {
    position: absolute;
    left: 55px;
    top: 320px;
    list-style: none;
    font-family: "Roboto", sans-serif;
    font-size: 21px;
    line-height: 31px;
    color: var(--ink);
  }
</style>
</head>
<body>
  <main class="canvas">
    <section class="business-card">
      <div class="brand-block">
        <div class="brand-name">Castlereagh Yard Works L.L.C.</div>
        <div class="brand-tagline">REPAIR - MAINTENANCE - IMPROVEMENT</div>
      </div>
      <div class="name-band">
        <span class="holder-name">PATRICK DUNLEAVY</span>
      </div>
      <ul class="contact-list">
        <li class="contact-phone">555.019.4826</li>
        <li class="contact-email">pat@castlereaghyardworks.example</li>
      </ul>
    </section>
  </main>
</body>
</html>
```